Ebook cover design for SPY THRILLER

An eBook cover is needed for a spy thriller. Good books to reference are Marcus Trevellyn and Harold Quimsby. We are after something cutting-edge, dramatic, stylish, and that stands out above the rest.

Title: The Grey Falcon: Ember's Throne (The Grey Falcon is the series).
Author: Dominic Velustro

The book is about a spy who goes undercover to stop an organ harvesting operation in Hungary. The name Dominic can be in white, and Velustro in shiny gold. Also feel free to make "The Grey Falcon" in shiny gold as well, and "Ember's Throne" in any way you think will look good (i.e. Red). Thick font would be good.

The winner of this will also have the privlege of creating the next 6 covers in the series, as they come about.

This project is suitable for designers who have experience creating eBook covers to Brindlemart's standard, and enjoy creating new, stand-out designs which really help the book stand tall above the rest.

```html
<!DOCTYPE html>
<html lang="en">
<head>
<meta charset="utf-8">
<title>The Grey Falcon: Ember's Throne — Dominic Velustro</title>
<link rel="stylesheet" href="https://fonts.googleapis.com/css2?family=Audiowide&family=Russo+One&display=swap">
<style>
  :root {
    --page-bg: #eeeeec;
    --cover-bg: #050505;
    --gold-light: #fff3b0;
    --gold-mid: #f2c94c;
    --gold-deep: #b8801e;
    --red-light: #ff8a95;
    --red-mid: #e8323f;
    --red-deep: #a3101c;
    --sky-top: #0a0a08;
    --sky-glow: #cfc98a;
    --sky-horizon: #e6df9c;
    --city-dark: #121209;
  }
  * { margin: 0; padding: 0; box-sizing: border-box; }
  html, body {
    width: 1200px;
    height: 1200px;
    overflow: hidden;
    background: var(--page-bg);
  }
  .canvas {
    width: 1200px;
    height: 1200px;
    display: flex;
    align-items: center;
    justify-content: center;
  }
  .cover {
    position: relative;
    width: 850px;
    height: 1130px;
    background: var(--cover-bg);
    overflow: hidden;
    text-align: center;
  }
  .gold-text {
    background: linear-gradient(180deg, var(--gold-light) 0%, var(--gold-mid) 45%, var(--gold-deep) 55%, var(--gold-mid) 80%, var(--gold-light) 100%);
    -webkit-background-clip: text;
    background-clip: text;
    color: transparent;
  }
  .series-title {
    position: absolute;
    top: 52px;
    left: 0;
    right: 0;
    font-family: "Russo One", sans-serif;
    font-size: 70px;
    letter-spacing: 1px;
    line-height: 1;
  }
  .book-title {
    position: absolute;
    top: 150px;
    left: 0;
    right: 0;
    font-family: "Russo One", sans-serif;
    font-size: 138px;
    line-height: 0.98;
    transform: skewX(-10deg);
    background: linear-gradient(180deg, var(--red-light) 0%, var(--red-mid) 40%, var(--red-deep) 55%, var(--red-mid) 75%, var(--red-light) 100%);
    -webkit-background-clip: text;
    background-clip: text;
    color: transparent;
  }
  .book-title span { display: block; }
  .skyline {
    position: absolute;
    top: 470px;
    left: 0;
    width: 100%;
    height: 300px;
    background:
      linear-gradient(180deg, transparent 0%, transparent 70%, var(--city-dark) 82%, var(--cover-bg) 100%),
      linear-gradient(180deg, var(--sky-top) 0%, #3a3826 25%, var(--sky-glow) 55%, var(--sky-horizon) 68%, #4a4630 80%, var(--cover-bg) 100%);
  }
  .author {
    position: absolute;
    left: 0;
    right: 0;
    font-family: "Audiowide", sans-serif;
    line-height: 1;
  }
  .author-first { top: 790px; font-size: 128px; letter-spacing: 4px; }
  .author-last { top: 940px; font-size: 116px; letter-spacing: 3px; }
</style>
</head>
<body>
  <main class="canvas">
    <article class="cover">
      <h2 class="series-title gold-text">THE GREY FALCON</h2>
      <h1 class="book-title"><span>EMBER'S</span><span>THRONE</span></h1>
      <div class="skyline" role="img" aria-label="Dusk view of a European city skyline with spires silhouetted against a pale yellow sky"></div>
      <p class="author author-first gold-text">DOMINIC</p>
      <p class="author author-last gold-text">VELUSTRO</p>
    </article>
  </main>
</body>
</html>
```